Jolly Paws Business Card Update

I have a business card which I love. I want to keep the same logo, colours, font and style. I want to upgrade the scripting and remove some elements and add others.
On the front side under Services - remove the existing wording and insert - Providing individual coaching strategies to create happy, healthy and social canine companions
Under Rebecca Thornbury amend the current wording to read: Qualified in Dog Behavioural Training, Natural Animal Healthcare and Animal Health Science
On the reverse side to remove the web address.

```html
<!DOCTYPE html>
<html lang="en">
<head>
<meta charset="utf-8">
<title>Jolly Paws Business Card</title>
<link rel="stylesheet" href="https://fonts.googleapis.com/css2?family=Arimo:wght@400;700&display=swap">
<style>
  :root {
    --sky: #3fb6e4;
    --azure: #139fd8;
    --cobalt: #0b6db4;
    --navy: #233e93;
    --violet: #4159a8;
    --crimson: #e22a30;
    --maroon: #7d1217;
    --wine: #8a3438;
    --cream: #efe7c9;
    --ink: #1d1d1d;
    --paper: #ffffff;
  }
  * { margin: 0; padding: 0; box-sizing: border-box; }
  html, body { width: 1200px; height: 800px; overflow: hidden; background: var(--paper); }
  body { font-family: "Arimo", Arial, sans-serif; position: relative; }

  .card {
    position: absolute;
    width: 540px;
    height: 310px;
    border-radius: 22px;
    overflow: hidden;
    box-shadow: 0 6px 14px rgba(0,0,0,0.22);
  }
  .card--front { left: 40px; top: 245px; }
  .card--back { left: 620px; top: 245px; }
  .card__bg { position: absolute; inset: 0; width: 100%; height: 100%; }

  /* Front */
  .brand-mark {
    position: absolute; left: 50%; top: 40px; transform: translateX(-50%);
    width: 104px; height: 104px; border-radius: 50%;
    background: var(--cream); border: 7px solid var(--crimson);
  }
  .brand-name {
    position: absolute; left: 0; right: 0; top: 160px; text-align: center;
    font-weight: 700; font-size: 38px; letter-spacing: 2px; text-transform: uppercase;
    color: var(--cream);
  }
  .brand-tagline {
    position: absolute; left: 0; right: 0; top: 206px; text-align: center;
    font-size: 15px; letter-spacing: 1.5px; color: var(--cream);
  }

  /* Back */
  .back-mark {
    position: absolute; left: 74px; top: 42px;
    width: 94px; height: 94px; border-radius: 50%;
    background: var(--cream); border: 6px solid var(--crimson);
  }
  .back-brand {
    position: absolute; left: 44px; width: 154px; top: 143px; text-align: center;
    font-weight: 700; font-size: 14px; color: var(--cream); text-transform: uppercase; letter-spacing: 1px;
  }
  .divider { position: absolute; background: var(--cream); width: 1px; }
  .divider--services { left: 212px; top: 30px; height: 126px; }
  .divider--contact { left: 318px; top: 214px; height: 66px; }

  .services { position: absolute; left: 228px; top: 36px; right: 24px; color: var(--cream); }
  .services__title { font-size: 17px; letter-spacing: 0.5px; margin-bottom: 6px; }
  .services__text { font-size: 13px; line-height: 1.35; }

  .mission {
    position: absolute; left: 0; right: 0; top: 170px; height: 20px;
    line-height: 20px; text-align: center; font-size: 12px; color: var(--ink);
  }

  .person { position: absolute; left: 16px; width: 292px; top: 206px; text-align: center; color: var(--cream); }
  .person__name { font-size: 20px; margin-bottom: 4px; }
  .person__creds { font-size: 11.5px; line-height: 1.3; }

  .contact { position: absolute; left: 332px; top: 222px; color: var(--cream); font-size: 13px; }
  .contact__row { display: flex; align-items: center; gap: 7px; margin-bottom: 9px; }
  .contact__icon { width: 16px; height: 16px; flex: none; }
</style>
</head>
<body>

<section class="card card--front" aria-label="Business card front">
  <svg class="card__bg" viewBox="0 0 540 310" preserveAspectRatio="none" aria-hidden="true">
    <defs>
      <linearGradient id="front-blue" x1="0.8" y1="0" x2="0.2" y2="1">
        <stop offset="0" stop-color="var(--sky)"/>
        <stop offset="0.45" stop-color="var(--azure)"/>
        <stop offset="0.75" stop-color="var(--cobalt)"/>
        <stop offset="1" stop-color="var(--navy)"/>
      </linearGradient>
      <linearGradient id="front-red" x1="0" y1="0" x2="1" y2="0">
        <stop offset="0" stop-color="var(--maroon)"/>
        <stop offset="0.5" stop-color="var(--crimson)"/>
        <stop offset="1" stop-color="var(--wine)"/>
      </linearGradient>
    </defs>
    <rect width="540" height="310" fill="url(#front-blue)"/>
    <path d="M0 300 C140 250 320 230 540 225 L540 310 L0 310 Z" fill="var(--cream)"/>
    <path d="M0 305 C140 256 320 236 540 231 L540 310 L0 310 Z" fill="url(#front-red)"/>
  </svg>
  <div class="brand-mark" aria-hidden="true"></div>
  <h1 class="brand-name">Jolly Paws</h1>
  <p class="brand-tagline">HAPPY DOGS, HAPPY OWNERS</p>
</section>

<section class="card card--back" aria-label="Business card back">
  <svg class="card__bg" viewBox="0 0 540 310" preserveAspectRatio="none" aria-hidden="true">
    <defs>
      <linearGradient id="back-blue" x1="0.8" y1="0" x2="0.2" y2="1">
        <stop offset="0" stop-color="var(--sky)"/>
        <stop offset="0.6" stop-color="var(--azure)"/>
        <stop offset="1" stop-color="var(--cobalt)"/>
      </linearGradient>
      <linearGradient id="back-red" x1="0" y1="1" x2="1" y2="0">
        <stop offset="0" stop-color="var(--maroon)"/>
        <stop offset="0.45" stop-color="var(--crimson)"/>
        <stop offset="1" stop-color="var(--wine)"/>
      </linearGradient>
    </defs>
    <rect width="540" height="170" fill="url(#back-blue)"/>
    <rect y="170" width="540" height="20" fill="var(--cream)"/>
    <rect y="190" width="540" height="120" fill="url(#back-red)"/>
  </svg>

  <div class="back-mark" aria-hidden="true"></div>
  <p class="back-brand">Jolly Paws</p>
  <span class="divider divider--services"></span>

  <div class="services">
    <h2 class="services__title">SERVICES</h2>
    <p class="services__text">Providing individual coaching strategies to create happy, healthy and social canine companions</p>
  </div>

  <p class="mission">Promoting communication and connection between dogs and their families</p>

  <div class="person">
    <h2 class="person__name">Rebecca Thornbury</h2>
    <p class="person__creds">Qualified in Dog Behavioural Training, Natural Animal Healthcare and Animal Health Science</p>
  </div>

  <span class="divider divider--contact"></span>

  <div class="contact">
    <p class="contact__row">
      <svg class="contact__icon" viewBox="0 0 16 16" aria-hidden="true">
        <circle cx="8" cy="8" r="7.5" fill="var(--cream)"/>
        <rect x="5.5" y="3.5" width="5" height="9" rx="1" fill="none" stroke="var(--crimson)" stroke-width="1.2"/>
        <line x1="7" y1="11" x2="9" y2="11" stroke="var(--crimson)" stroke-width="1"/>
      </svg>
      <span>0412 555 019</span>
    </p>
    <p class="contact__row">
      <svg class="contact__icon" viewBox="0 0 16 16" aria-hidden="true">
        <circle cx="8" cy="8" r="7.5" fill="var(--cream)"/>
        <rect x="4" y="5" width="8" height="6" fill="none" stroke="var(--crimson)" stroke-width="1.2"/>
        <polyline points="4,5 8,8.5 12,5" fill="none" stroke="var(--crimson)" stroke-width="1.2"/>
      </svg>
      <span>jollypaws1@example.com</span>
    </p>
  </div>
</section>

</body>
</html>
```